Business Card for a Little Gothic Online Shoe Business
Velvet Moth Treasures
Business Card for a Little Gothic Online Shoe Business - Apparel
Creative Brief
Bright & Fun-filled
9 Carrowby Street Kelvin Flats QLD 4826
velvetmothtreasures@mailbrook.net
www.velvetmothtreasures-shop.com.au
ABN: 41 285 607 952
In addition to Business card designs I would also like to see designs for Letterhead and Envelope.
This should be a really funky fresh design to match the Business Logo. Our Colours are Purple and Black but Im open to others as long as the Business Logo is not changed. I also like the idea of incorpating Candy Striping or Old Victorian Floral Motifs in the Card I do not want any Shoes on the card as we also do Clothes etc

```html
<!DOCTYPE html>
<html lang="en">
<head>
<meta charset="utf-8">
<title>Velvet Moth Treasures — Stationery</title>
<link rel="stylesheet" href="https://fonts.googleapis.com/css2?family=Poppins:wght@400;600&display=swap">
<style>
  :root{
    --bg:#4c4d51;
    --purple:#5b2b93;
    --purple-deep:#462173;
    --paper:#f2f2f4;
    --ink:#2a2a2e;
  }
  *{margin:0;padding:0;box-sizing:border-box}
  html,body{width:1200px;height:677px;overflow:hidden}
  body{background:var(--bg);font-family:"Poppins",sans-serif;color:var(--ink);position:relative}
  .piece{position:absolute;overflow:hidden}
  .piece svg.shapes{position:absolute;inset:0;width:100%;height:100%}
  .brand{position:absolute;display:flex;align-items:center;gap:6px;color:var(--purple);font-weight:600;line-height:1.1}
  .brand-dot{border-radius:50%;background:var(--purple);flex:none}
  .contact{position:absolute;font-size:6.5px;line-height:1.55;color:var(--ink)}

  /* letterhead */
  .letterhead{left:380px;top:70px;width:370px;height:523px;background:var(--paper)}
  .letterhead .brand{right:24px;top:20px;font-size:11px}
  .letterhead .brand-dot{width:14px;height:14px}
  .letterhead .contact{left:30px;bottom:60px}

  /* business cards */
  .card{left:40px;width:300px;height:175px;background:var(--paper)}
  .card-front{top:250px}
  .card-back{top:445px}
  .card .brand{font-size:13px}
  .card .brand-dot{width:16px;height:16px}
  .card-front .brand{left:26px;top:26px}
  .card-front .contact{left:26px;top:64px;color:var(--ink)}
  .card-back .brand{left:50%;top:52px;transform:translateX(-50%)}
  .card-back .tagline{position:absolute;left:0;right:0;top:80px;text-align:center;font-size:7px;color:var(--purple)}

  /* envelope */
  .envelope{left:780px;top:60px;width:390px;height:200px;background:var(--purple)}
  .envelope .brand{left:34px;top:34px;font-size:12px}
  .envelope .brand-dot{width:15px;height:15px}
  .envelope .contact{left:34px;top:66px}

  /* disc */
  .disc{left:860px;top:320px;width:250px;height:250px;border-radius:50%;background:var(--purple)}
  .disc .brand{left:50%;top:46px;transform:translateX(-50%);font-size:11px;white-space:nowrap}
  .disc .brand-dot{width:13px;height:13px}
</style>
</head>
<body>

<!-- Letterhead -->
<section class="piece letterhead">
  <svg class="shapes" viewBox="0 0 370 523" aria-hidden="true">
    <path d="M170 0 H370 V78 H170 Z" fill="var(--purple)"/>
    <g fill="var(--paper)">
      <rect x="186" y="0" width="184" height="50"/>
      <circle cx="200" cy="44" r="18"/>
      <circle cx="232" cy="54" r="18"/>
      <circle cx="266" cy="56" r="18"/>
      <circle cx="300" cy="54" r="18"/>
      <circle cx="334" cy="50" r="18"/>
      <circle cx="362" cy="44" r="16"/>
    </g>
  </svg>
  <div class="brand"><span class="brand-dot"></span>Velvet Moth Treasures</div>
  <p class="contact">
    9 Carrowby Street Kelvin Flats QLD 4826<br>
    velvetmothtreasures@mailbrook.net<br>
    www.velvetmothtreasures-shop.com.au<br>
    ABN: 41 285 607 952
  </p>
</section>

<!-- Business card front -->
<section class="piece card card-front">
  <svg class="shapes" viewBox="0 0 300 175" aria-hidden="true">
    <path d="M0 120 H300 V175 H0 Z" fill="var(--purple)"/>
    <g fill="var(--paper)">
      <circle cx="200" cy="118" r="20"/>
      <circle cx="236" cy="124" r="20"/>
      <circle cx="272" cy="118" r="20"/>
      <circle cx="164" cy="124" r="18"/>
    </g>
  </svg>
  <div class="brand"><span class="brand-dot"></span>Velvet Moth Treasures</div>
  <p class="contact">
    rowanpix<br>
    9 Carrowby Street Kelvin Flats QLD 4826<br>
    velvetmothtreasures@mailbrook.net<br>
    www.velvetmothtreasures-shop.com.au<br>
    ABN: 41 285 607 952
  </p>
</section>

<!-- Business card back -->
<section class="piece card card-back">
  <svg class="shapes" viewBox="0 0 300 175" aria-hidden="true">
    <path d="M0 118 H300 V175 H0 Z" fill="var(--purple)"/>
    <g fill="var(--paper)">
      <circle cx="40" cy="120" r="22"/>
      <circle cx="80" cy="126" r="20"/>
      <circle cx="120" cy="122" r="20"/>
    </g>
  </svg>
  <div class="brand"><span class="brand-dot"></span>Velvet Moth Treasures</div>
  <p class="tagline">www.velvetmothtreasures-shop.com.au</p>
</section>

<!-- Envelope -->
<section class="piece envelope">
  <svg class="shapes" viewBox="0 0 390 200" aria-hidden="true">
    <g fill="var(--paper)">
      <rect x="0" y="0" width="190" height="110"/>
      <rect x="0" y="0" width="215" height="70"/>
      <circle cx="215" cy="40" r="30"/>
      <circle cx="200" cy="88" r="26"/>
      <circle cx="160" cy="114" r="24"/>
      <circle cx="118" cy="122" r="22"/>
      <circle cx="76" cy="124" r="22"/>
      <circle cx="34" cy="122" r="22"/>
      <circle cx="0" cy="118" r="20"/>
    </g>
    <rect x="232" y="126" width="130" height="42" rx="3" fill="var(--purple-deep)"/>
  </svg>
  <div class="brand"><span class="brand-dot"></span>Velvet Moth Treasures</div>
  <p class="contact">
    9 Carrowby Street Kelvin Flats QLD 4826<br>
    velvetmothtreasures@mailbrook.net<br>
    www.velvetmothtreasures-shop.com.au
  </p>
</section>

<!-- Disc -->
<section class="piece disc">
  <svg class="shapes" viewBox="0 0 250 250" aria-hidden="true">
    <g fill="var(--paper)">
      <rect x="0" y="0" width="250" height="70"/>
      <circle cx="40" cy="72" r="22"/>
      <circle cx="82" cy="82" r="22"/>
      <circle cx="125" cy="86" r="22"/>
      <circle cx="168" cy="82" r="22"/>
      <circle cx="210" cy="72" r="22"/>
    </g>
    <circle cx="125" cy="125" r="30" fill="#d8d8dc"/>
    <circle cx="125" cy="125" r="11" fill="var(--bg)"/>
  </svg>
  <div class="brand"><span class="brand-dot"></span>Velvet Moth Treasures</div>
</section>

</body>
</html>
```